MOLT - Monitoring Natural Hazards from Space Web Application

KORVEN Sarl is a Luxembourg based Space-Startup that works in the field of Earth Observation. KORVEN is a platform able to extract value-added information from satellite data and is specialized in mapping Natural Disaster (floods, fires etc).

We are now developing a new vertical tool, called MOLT, dedicated to the monitoring of natural hazards in Humanitarian Camps around the world.

The goal of MOLT is to hide to the users' all the complexity of the Satellite Image processing and just provide them the results.

This project require to Design 4 pages of MOLT:
• Public Home Page (Code - V01)
• Dashboard (private Home Page) (Code - V03)
• Monitor (web GIS) (Code - V14)
• Registration Page (Code - V04)

We would like to provide the required time to make a good job.

Target Market(s)

Humanitarian Agencies, Goverments

Coding

Coded - Design and coding required

Number of Pages Required

4 page

Font styles to use
Other font styles liked:
• see the manual attached

Requirements
Must have
• 4 pages. One Home, one form, one dashboard and one web map.
Nice to have
• Please read the attachment with all the detailed instructions

```html
<!DOCTYPE html>
<html lang="en">
<head>
<meta charset="utf-8">
<title>MOLT – Dashboard</title>
<link href="https://fonts.googleapis.com/css2?family=Jost:wght@400;500&display=swap" rel="stylesheet">
<style>
:root{
  --navy:#284a5a;
  --navy-dark:#223f4d;
  --gold:#f2c14e;
  --gold-soft:#fff1d4;
  --ink:#1f2a30;
  --muted:#6b7378;
  --line:#e4e6e8;
  --chip:#9a9fa3;
  --alert-bg:#fbd3d3;
  --alert-red:#d8262f;
  --sea:#6fd3e6;
  --land:#a8dcb7;
  --white:#ffffff;
}
*{box-sizing:border-box;margin:0;padding:0}
html,body{width:1200px;height:827px;overflow:hidden}
body{font-family:"Jost",sans-serif;color:var(--ink);background:var(--sea);position:relative}
.map{position:absolute;left:0;top:49px;width:1200px;height:778px;
  background:linear-gradient(110deg,#9fd6b2 0%,#7fd2d8 30%,var(--sea) 55%,#86d7d6 72%,#cfe8c8 88%,#eee9df 100%)}
.topbar{position:absolute;left:0;top:0;width:1200px;height:49px;background:var(--navy);display:flex;align-items:center}
.brand{position:absolute;left:20px;top:13px;display:flex;align-items:center;gap:6px;color:var(--gold);font-size:14px;font-weight:500}
.brand-dot{width:22px;height:22px;border:2px solid var(--gold);border-radius:50%}
.nav{position:absolute;left:528px;top:9px;display:flex;gap:14px}
.nav-item{display:flex;align-items:center;gap:8px;height:31px;padding:0 11px;font-size:12.5px;color:#cfd7db;border-radius:3px}
.nav-item.active{border:1px solid var(--gold);color:var(--gold)}
.avatar{position:absolute;left:1151px;top:13px;width:22px;height:22px;border-radius:50%;background:linear-gradient(135deg,#e6b98d,#9b6a48)}
.panel{position:absolute;left:13px;top:67px;width:300px;height:780px;background:var(--white);border-radius:6px;padding:18px 20px}
.panel h1{font-size:15.5px;font-weight:400;margin-bottom:7px}
.filter{display:flex;align-items:center;gap:6px;font-size:10px;color:var(--muted)}
.chip{display:inline-flex;align-items:center;height:20px;padding:0 7px;border:1px solid var(--chip);border-radius:10px;font-size:9.5px;color:var(--muted)}
.chip.on{background:var(--navy);border-color:var(--navy);color:var(--white);padding:0 9px}
.card{border:1px solid var(--line);border-radius:4px;padding:18px 16px;margin-top:17px}
.card-title{font-size:11.5px}
.stat{display:flex;align-items:center;gap:8px;margin-top:16px;font-size:25px;font-weight:400}
.trend{font-size:9px;margin-top:2px}
.bars{position:relative;height:75px;margin-top:14px;border-bottom:1px solid var(--line)}
.bar{position:absolute;bottom:0;width:34px;background:linear-gradient(180deg,var(--gold),var(--gold-soft))}
.bar-labels{position:relative;height:12px;font-size:5px;color:var(--muted)}
.bar-labels span{position:absolute;top:4px}
.event{display:flex;align-items:center;gap:6px;font-size:11px;margin-top:18px}
.event b{font-weight:500;color:var(--navy)}
.event-chips{display:flex;gap:8px;margin-top:6px}
.alerts-tag{display:inline-flex;align-items:center;gap:8px;margin-top:17px;height:28px;padding:0 10px;background:var(--alert-bg);border-radius:3px;font-size:15px}
.alert{display:flex;gap:7px;border:1px solid var(--line);border-radius:4px;padding:7px;margin-top:12px;height:70px}
.alert-photo{width:57px;height:57px;flex:none;border-radius:2px;background:linear-gradient(180deg,#8fc3e0,#9aa48e 60%,#6b6a5c)}
.alert h3{font-size:9.8px;font-weight:400;line-height:1.35}
.alert p{font-size:7.2px;line-height:1.5;margin-top:4px}
.tools{position:absolute;left:1130px;top:73px;width:56px;background:var(--white);border-radius:5px;padding:10px 0;display:flex;flex-direction:column;align-items:center;gap:26px}
.tool-box{position:absolute;left:1130px;width:56px;background:var(--white);border-radius:5px;display:flex;flex-direction:column;align-items:center;justify-content:center;gap:28px}
.pin{position:absolute}
</style>
</head>
<body>
<div class="map" role="img" aria-label="Map of the North Atlantic showing the Americas, Europe and West Africa"></div>

<svg class="pin" style="left:403px;top:319px" width="26" height="36" viewBox="0 0 26 36"><path d="M13 35C5 24 1 19 1 13a12 12 0 0124 0c0 6-4 11-12 22z" fill="var(--navy)"/><circle cx="13" cy="13" r="6" fill="#fff"/><circle cx="13" cy="13" r="4" fill="var(--navy)"/><circle cx="13" cy="13" r="3" fill="#fff"/></svg>
<svg class="pin" style="left:419px;top:490px" width="26" height="36" viewBox="0 0 26 36"><path d="M13 35C5 24 1 19 1 13a12 12 0 0124 0c0 6-4 11-12 22z" fill="var(--navy)"/><circle cx="13" cy="13" r="6" fill="#fff"/><circle cx="13" cy="13" r="4" fill="var(--navy)"/><circle cx="13" cy="13" r="3" fill="#fff"/></svg>
<svg class="pin" style="left:458px;top:650px" width="26" height="36" viewBox="0 0 26 36"><path d="M13 35C5 24 1 19 1 13a12 12 0 0124 0c0 6-4 11-12 22z" fill="var(--navy)"/><circle cx="13" cy="13" r="6" fill="#fff"/><circle cx="13" cy="13" r="4" fill="var(--navy)"/><circle cx="13" cy="13" r="3" fill="#fff"/></svg>
<svg class="pin" style="left:1057px;top:108px" width="26" height="36" viewBox="0 0 26 36"><path d="M13 35C5 24 1 19 1 13a12 12 0 0124 0c0 6-4 11-12 22z" fill="var(--navy)"/><circle cx="13" cy="13" r="6" fill="#fff"/><circle cx="13" cy="13" r="4" fill="var(--navy)"/><circle cx="13" cy="13" r="3" fill="#fff"/></svg>

<header class="topbar">
  <div class="brand"><span class="brand-dot"></span>MOLT</div>
  <nav class="nav">
    <div class="nav-item active">
      <svg width="16" height="16" viewBox="0 0 16 16" fill="none" stroke="currentColor" stroke-width="1.3"><rect x="1" y="1" width="5.5" height="5.5" rx="1.5"/><rect x="9.5" y="1" width="5.5" height="5.5" rx="1.5"/><rect x="1" y="9.5" width="5.5" height="5.5" rx="1.5"/><rect x="9.5" y="9.5" width="5.5" height="5.5" rx="1.5"/></svg>
      Dashboard
    </div>
    <div class="nav-item">
      <svg width="14" height="14" viewBox="0 0 14 14" fill="none" stroke="currentColor" stroke-width="1.2"><rect x="1" y="1" width="12" height="12" rx="1"/><path d="M4 4v4M7 4v6M10 4v3"/></svg>
      Monitor
    </div>
  </nav>
  <div class="avatar" role="img" aria-label="User profile picture"></div>
</header>

<aside class="panel">
  <h1>Areas of operations</h1>
  <div class="filter">Showing
    <span class="chip on">All</span><span class="chip">USA</span><span class="chip">UK</span><span class="chip">Brazil</span><span class="chip">Cuba</span>
  </div>

  <section class="card" style="height:185px">
    <div class="card-title">No. of People Affected</div>
    <div class="stat">
      <svg width="26" height="22" viewBox="0 0 26 22" fill="var(--navy)"><circle cx="16" cy="6" r="5"/><path d="M8 22c0-6 4-9 8-9s9 3 9 9z"/><circle cx="8" cy="8" r="4.5"/><path d="M0 22c0-5 3-8 8-8 2 0 3 .5 4 1-2 2-3 4-3 7z"/></svg>
      1,200,136
    </div>
    <div class="trend">▲ &nbsp;+20% vs last week</div>
    <div class="bars">
      <div class="bar" style="left:7px;height:55px"></div>
      <div class="bar" style="left:70px;height:44px"></div>
      <div class="bar" style="left:133px;height:36px"></div>
    </div>
    <div class="bar-labels"><span style="left:14px">Week 1</span><span style="left:76px">Week 2</span><span style="left:140px">Week 3</span><span style="left:203px">Week 4</span></div>
  </section>

  <section class="card" style="height:185px;padding:22px 20px">
    <div class="card-title">Recent Ongoing Events</div>
    <div class="event">
      <svg width="18" height="14" viewBox="0 0 18 14" fill="var(--navy)"><path d="M2 7l7-5 7 5z"/><path d="M1 10q2-2 4 0t4 0 4 0 4 0v1q-2 2-4 0t-4 0-4 0-4 0z"/><path d="M1 13q2-2 4 0t4 0 4 0 4 0v1H1z"/></svg>
      Floods in <b>2 Areas</b></div>
    <div class="event-chips"><span class="chip">Brazil</span><span class="chip">Cuba</span></div>
    <div class="event" style="margin-top:22px">
      <svg width="18" height="16" viewBox="0 0 18 16" fill="none" stroke="var(--navy)" stroke-width="2"><path d="M9 8c-5-1-7-4-5-7M9 8c5 1 7 4 5 7M9 8c1-5 4-7 8-5M9 8c-1 5-4 7-8 5"/></svg>
      Hurricanes in <b>2 Areas</b></div>
    <div class="event-chips"><span class="chip">USA</span><span class="chip">UK</span></div>
  </section>

  <div class="alerts-tag">
    <svg width="18" height="16" viewBox="0 0 18 16" fill="none" stroke="var(--alert-red)" stroke-width="1.5"><path d="M9 1l8 14H1z" stroke-linejoin="round"/><path d="M9 6v4M9 12v1"/></svg>
    Alerts</div>

  <article class="alert"><div class="alert-photo" role="img" aria-label="Photo of a flooded street"></div><div><h3>Massive Floods Hit Cuba — Thousands Displaced</h3><p>Severe monsoon rains trigger widespread flooding across several towns in Cuba.</p></div></article>
  <article class="alert"><div class="alert-photo" role="img" aria-label="Photo of a vehicle driving through floodwater"></div><div><h3>Massive Floods Hit Cuba — Thousands Displaced</h3><p>Severe monsoon rains trigger widespread flooding across several towns in Cuba.</p></div></article>
  <article class="alert"><div class="alert-photo" role="img" aria-label="Photo of a flooded street"></div><div><h3>Massive Floods Hit Cuba — Thousands Displaced</h3><p>Severe monsoon rains trigger widespread flooding across several towns in Cuba.</p></div></article>
</aside>

<div class="tools" style="height:187px">
  <svg width="16" height="16" viewBox="0 0 16 16" fill="var(--navy)"><path d="M8 0l1.5 2.2 2.6-.6.6 2.6L15 5.7 13.9 8 15 10.3l-2.3 1.5-.6 2.6-2.6-.6L8 16l-1.5-2.2-2.6.6-.6-2.6L1 10.3 2.1 8 1 5.7l2.3-1.5.6-2.6 2.6.6z"/><circle cx="8" cy="8" r="2.5" fill="#fff"/></svg>
  <svg width="18" height="16" viewBox="0 0 18 16" fill="none" stroke="var(--navy)" stroke-width="1.4"><path d="M1 3h9M5.5 1v2M3 3q1 5 6 7M8 3q-1 5-6 8M9 15l3.5-9 3.5 9M10.2 12h4.6"/></svg>
  <svg width="18" height="18" viewBox="0 0 18 18"><circle cx="9" cy="9" r="7" fill="none" stroke="var(--navy)" stroke-width="4"/><path d="M4 4l3 3M14 4l-3 3M4 14l3-3M14 14l-3-3" stroke="#fff" stroke-width="1.5"/></svg>
  <svg width="16" height="16" viewBox="0 0 16 16" fill="var(--navy)"><path d="M8 1a7 7 0 100 14z"/><path d="M9 5l4 3-4 3z"/></svg>
</div>
<div class="tool-box" style="top:627px;height:55px">
  <svg width="20" height="20" viewBox="0 0 20 20" fill="none" stroke="var(--ink)" stroke-width="1.4" stroke-linejoin="round"><path d="M10 2l8 4-8 4-8-4z"/><path d="M2 10l8 4 8-4M2 14l8 4 8-4"/></svg>
</div>
<div class="tool-box" style="top:693px;height:100px">
  <svg width="18" height="18" viewBox="0 0 18 18" fill="none" stroke="var(--ink)" stroke-width="1.5"><circle cx="7.5" cy="7.5" r="6"/><path d="M12 12l5 5M5 7.5h5M7.5 5v5"/></svg>
  <svg width="18" height="18" viewBox="0 0 18 18" fill="none" stroke="var(--ink)" stroke-width="1.5"><circle cx="7.5" cy="7.5" r="6"/><path d="M12 12l5 5M5 7.5h5"/></svg>
</div>
</body>
</html>
```